Hal's Remedies Business Card Design Project

I need a business card designed for my pharmacy Hal's Remedies. I would like just the logo on one side, maybe with black background and white lettering. The other side I would also like to include my logo which is attached. Also, please include my name and the following information:
Hal Norwick Owner/Pharm D.
Business address is 7163 N Birch Rd Sioux Falls, SD 57291.
Phone number is 605-318-6027 and fax # is 605-318-6031.
my email address is hal@halsremedies.example.
My website is www.halsremedies.example.
My business hours are Monday-Friday 8am-7 pm. Saturday 8am-12 pm. Sunday Closed.
I would like the design to include my logo colors, black, white, and neon green. Silver may be added as a highlight. Thanks.
Pharmacy
See above in product description

```html
<!DOCTYPE html>
<html lang="en">
<head>
<meta charset="utf-8">
<title>Hal's Remedies – Business Card</title>
<link rel="stylesheet" href="https://fonts.googleapis.com/css2?family=Lato:wght@400;700&display=swap">
<style>
  :root {
    --stage: #2a2a2c;
    --card-black: #0b0b0b;
    --card-white: #ffffff;
    --ink: #1a1a1a;
    --neon: #8cc63f;
    --silver: #d9d9d9;
    --white: #ffffff;
  }
  * { box-sizing: border-box; margin: 0; padding: 0; }
  html, body {
    width: 1200px;
    height: 800px;
    overflow: hidden;
    background: var(--stage);
    font-family: "Lato", sans-serif;
  }
  .stage {
    width: 1200px;
    height: 800px;
    display: flex;
    align-items: center;
    justify-content: center;
    gap: 40px;
  }
  .card {
    position: relative;
    width: 540px;
    height: 309px;
    border-radius: 2px;
    box-shadow: 0 10px 24px rgba(0,0,0,0.45);
  }
  /* Front */
  .card--front {
    background: var(--card-black);
    display: flex;
    align-items: center;
    justify-content: center;
    gap: 22px;
  }
  .brand-dot {
    width: 30px;
    height: 30px;
    border-radius: 50%;
    background: var(--neon);
  }
  .brand-divider {
    width: 1px;
    height: 58px;
    background: var(--silver);
  }
  .brand-name {
    color: var(--white);
    font-weight: 700;
    font-size: 34px;
    letter-spacing: -0.5px;
  }
  /* Back */
  .card--back {
    background: var(--card-white);
    color: var(--ink);
  }
  .holder {
    position: absolute;
    left: 40px;
    top: 62px;
  }
  .holder-name {
    color: var(--neon);
    font-weight: 700;
    font-size: 22px;
    line-height: 1.1;
  }
  .holder-title {
    font-size: 12px;
    font-weight: 700;
    margin-top: 3px;
  }
  .address {
    position: absolute;
    left: 40px;
    top: 190px;
    font-size: 16px;
    font-weight: 700;
    line-height: 1.3;
  }
  .contacts {
    position: absolute;
    left: 300px;
    top: 66px;
    list-style: none;
    font-size: 14px;
    line-height: 1;
  }
  .contacts li {
    display: flex;
    align-items: center;
    gap: 10px;
    margin-bottom: 6px;
  }
  .contacts svg {
    width: 12px;
    height: 12px;
    flex: none;
    fill: var(--neon);
  }
</style>
</head>
<body>
<main class="stage">
  <section class="card card--front" aria-label="Card front">
    <span class="brand-dot"></span>
    <span class="brand-divider"></span>
    <span class="brand-name">Hal's Remedies</span>
  </section>

  <section class="card card--back" aria-label="Card back">
    <div class="holder">
      <p class="holder-name">Hal Norwick</p>
      <p class="holder-title">Owner/Pharm D.</p>
    </div>

    <p class="address">7163 N Birch Rd Sioux Falls,<br>SD 57291.</p>

    <ul class="contacts">
      <li>
        <svg viewBox="0 0 12 12" aria-hidden="true"><path d="M1 3.5C1 2 2 1 3.5 1h5C10 1 11 2 11 3.5V4H8.5V3h-5v1H1z M2 5h8l1 5H1z M4.5 6.5h3v2h-3z"/></svg>
        605-318-6027
      </li>
      <li>
        <svg viewBox="0 0 12 12" aria-hidden="true"><path d="M3 1h6v3H3z M1 4.5h10V9H9v2H3V9H1z M4 8v2h4V8z"/></svg>
        605-318-6031.
      </li>
      <li>
        <svg viewBox="0 0 12 12" aria-hidden="true"><path d="M1 2.5h10v7H1z M1.5 3L6 6.5 10.5 3" stroke="#fff" stroke-width="0.9"/></svg>
        hal@halsremedies.example.
      </li>
      <li>
        <svg viewBox="0 0 12 12" aria-hidden="true"><circle cx="6" cy="6" r="5"/><path d="M1 6h10M6 1c-2 2.5-2 7.5 0 10M6 1c2 2.5 2 7.5 0 10" stroke="#fff" stroke-width="0.7" fill="none"/></svg>
        www.halsremedies.example.
      </li>
    </ul>
  </section>
</main>
</body>
</html>
```